Letter and Envelope Design For Larchmont Realty

Please design a letter and an envelope incorporating our logo (See Attached). We are also launched a business card contest. Since we want them to match, please feel free to submit a design for both the business card and also the letter design and envelope.

Requirements
Must have
• The envelope, the letter and the business cards must match somehow connecting the designs. We want them to have something that holds them together besides the logo.

```html
<!DOCTYPE html>
<html lang="en">
<head>
<meta charset="utf-8">
<title>Larchmont Realty – Letterhead and Envelope</title>
<link href="https://fonts.googleapis.com/css2?family=Roboto:wght@400;500;700&display=swap" rel="stylesheet">
<style>
  :root {
    --backdrop: #666666;
    --paper: #f6f6f4;
    --navy: #00198a;
    --ink: #4a4a4a;
    --text-grey: #7a7a7a;
    --watermark: #e6e6e4;
    --rule: #5a6bbf;
  }
  * { margin: 0; padding: 0; box-sizing: border-box; }
  html, body { width: 1200px; height: 816px; overflow: hidden; }
  body {
    background: var(--backdrop);
    font-family: 'Roboto', Arial, sans-serif;
    position: relative;
  }
  .sheet {
    position: absolute;
    background: var(--paper);
    overflow: hidden;
  }
  .watermark-ring {
    position: absolute;
    border-radius: 50%;
    border: 8px solid var(--watermark);
  }
  .brand {
    position: absolute;
    display: flex;
    align-items: center;
    gap: 9px;
  }
  .brand-dot {
    width: 32px; height: 32px;
    border-radius: 50%;
    border: 2px solid var(--navy);
    flex: none;
  }
  .brand-name {
    color: var(--navy);
    font-weight: 500;
    font-size: 13px;
    letter-spacing: 1.6px;
    line-height: 13px;
    text-transform: uppercase;
  }
  .brand-name span { display: block; font-size: 9px; letter-spacing: 3px; text-align: center; margin-top: 3px; }

  /* Envelope front */
  .envelope-front { left: 140px; top: 221px; width: 474px; height: 212px; }
  .envelope-front .watermark-ring { left: 272px; top: -20px; width: 240px; height: 240px; }
  .envelope-front .brand { left: 23px; top: 26px; }
  .return-address {
    position: absolute; left: 34px; top: 69px;
    font-size: 6.6px; color: #222;
  }

  /* Envelope back */
  .envelope-back { left: 140px; top: 456px; width: 474px; height: 212px; }
  .envelope-flap { position: absolute; left: 0; top: 0; }
  .flap-name {
    position: absolute; left: 0; width: 474px; top: 26px;
    text-align: center; color: #fff; font-weight: 500;
    font-size: 11.5px; letter-spacing: 1.6px; line-height: 12px;
  }
  .flap-name span { display: block; font-size: 8px; letter-spacing: 3px; margin-top: 3px; }

  /* Letterhead */
  .letterhead { left: 667px; top: 130px; width: 391px; height: 554px; }
  .letterhead .watermark-ring { left: 73px; top: 154px; width: 248px; height: 248px; }
  .letterhead .brand { left: 27px; top: 36px; }
  .letter-body {
    position: absolute; left: 28px; top: 121px; width: 343px;
    font-size: 6.2px; line-height: 8.8px; color: var(--text-grey);
    letter-spacing: -0.05px;
  }
  .letter-date { margin-bottom: 18px; }
  .recipient { margin-bottom: 17px; }
  .recipient strong { color: var(--ink); font-weight: 700; }
  .salutation { margin-bottom: 9px; }
  .letter-body p.copy { text-align: justify; margin-bottom: 9px; }
  .sign-off { position: absolute; left: 28px; top: 423px; font-size: 6.4px; color: var(--text-grey); }
  .sign-off strong { color: var(--ink); font-weight: 700; display: block; }
  .signature {
    display: block; width: 90px; height: 18px; margin: 6px 0 6px 0;
    background: linear-gradient(90deg, #dfe3f3, #eef0f7);
    border-radius: 2px;
  }
  .footer-rule {
    position: absolute; left: 22px; top: 504px; width: 340px; height: 1px; background: var(--rule);
  }
  .contact {
    position: absolute; left: 0; width: 391px; top: 512px;
    text-align: center; font-size: 6.6px; line-height: 10px; color: #222;
  }
  .contact svg { width: 6px; height: 6px; vertical-align: -0.5px; margin: 0 2px 0 4px; fill: var(--navy); }
</style>
</head>
<body>

<section class="sheet envelope-front">
  <div class="watermark-ring"></div>
  <div class="brand">
    <div class="brand-dot"></div>
    <div class="brand-name">Larchmont<span>Realty</span></div>
  </div>
  <p class="return-address">234 Anywhere, Any City, Any Town, US 1234</p>
</section>

<section class="sheet envelope-back">
  <svg class="envelope-flap" width="474" height="80" viewBox="0 0 474 80">
    <path d="M0 0 H474 L446 62 Q438 76 414 76 H60 Q36 76 28 62 Z" fill="var(--navy)"/>
    <circle cx="237" cy="38" r="29" fill="none" stroke="#1a2f97" stroke-width="1.5"/>
  </svg>
  <div class="flap-name">LARCHMONT<span>REALTY</span></div>
</section>

<section class="sheet letterhead">
  <div class="watermark-ring"></div>
  <div class="brand">
    <div class="brand-dot"></div>
    <div class="brand-name">Larchmont<span>Realty</span></div>
  </div>

  <div class="letter-body">
    <p class="letter-date">30/20/2016</p>
    <p class="recipient"><strong>Mr. Alan Brooks</strong><br>123, Street No. 123,<br>City Name<br>Pincode-123456</p>
    <p class="salutation">Dear Sir,</p>
    <p class="copy">Lorem Ipsum is simply dummy text of the printing and typesetting industry. Lorem Ipsum has been the industry's standard dummy text ever since the 1500s, when an unknown printer took a galley of type and scrambled it to make a type specimen book. It has survived not only five centuries, but also the leap into electronic typesetting, remaining essentially unchanged. It was popularised in the 1960s with the release of transfer lettering sheets containing Lorem Ipsum passages, and more recently with desktop publishing software like page layout tools including versions of Lorem Ipsum.</p>
    <p class="copy">Lorem Ipsum is simply dummy text of the printing and typesetting industry. Lorem Ipsum has been the industry's standard dummy text ever since the 1500s, when an unknown printer took a galley of type and scrambled it to make a type specimen book. It has survived not only five centuries, but also the leap into electronic typesetting, remaining essentially unchanged. It was popularised in the 1960s with the release of transfer lettering sheets containing Lorem Ipsum passages, and more recently with desktop publishing software like page layout tools including versions of Lorem Ipsum.</p>
    <p class="copy">Lorem Ipsum is simply dummy text of the printing and typesetting industry. Lorem Ipsum has been the industry's standard dummy text ever since the 1500s, when an unknown printer took a galley of type and scrambled it to make a type specimen book.</p>
    <p class="copy">Lorem Ipsum is simply dummy text of the printing and typesetting industry. Lorem Ipsum has been the industry's standard dummy text ever since the 1500s, when an unknown printer took a galley of type and scrambled it to make a type specimen book.</p>
  </div>

  <div class="sign-off">
    <strong>Your Name</strong>
    <span class="signature" role="img" aria-label="Handwritten signature"></span>
    CEO &nbsp;|&nbsp; Owner
  </div>

  <div class="footer-rule"></div>
  <div class="contact">
    <svg viewBox="0 0 10 10"><path d="M2 0 L4 2.5 L3 4 Q4.5 6 6 7 L7.5 6 L10 8 L8.5 10 Q3 9 0 1.5 Z"/></svg>555.555.5555
    <svg viewBox="0 0 10 10"><rect x="0" y="2" width="10" height="7" rx="1"/></svg>office@larchmontrealty.example
    <svg viewBox="0 0 10 10"><circle cx="5" cy="5" r="5"/></svg>www.larchmontrealty.example<br>
    <svg viewBox="0 0 10 10"><path d="M5 0 A3.6 3.6 0 0 1 8.6 3.6 Q8.6 6 5 10 Q1.4 6 1.4 3.6 A3.6 3.6 0 0 1 5 0 Z"/></svg>234 Anywhere, Any City, Any Town, US 1234
  </div>
</section>

</body>
</html>
```